Bref créative
Business Cards - Skyline Assessors
Two sided business cards
Simple
Corwin Hask
Certified Appraiser
48270 Millbrook Lane #1174
Sterling, VA 20391
corwin@plumvexa.com
www.plumvexa.com
Just the logo, either include the text or not (what ever looks better)
Colors and Fonts Guide

```html
<!DOCTYPE html>
<html lang="en">
<head>
<meta charset="utf-8">
<title>Skyline Assessors – Business Card</title>
<link rel="stylesheet" href="https://fonts.googleapis.com/css2?family=Open+Sans:wght@400;600;700&display=swap">
<style>
  :root {
    --backdrop: #e9e6e1;
    --card-white: #ffffff;
    --brand-red: #8e1b20;
    --red-bright: #e2222b;
    --red-mid: #c0151d;
    --red-deep: #4f0c10;
    --swoosh-blue: #2f7fb4;
    --swoosh-navy: #183f66;
    --ink-light: #ffffff;
    --ink-soft: rgba(255,255,255,0.88);
  }
  * { margin: 0; padding: 0; box-sizing: border-box; }
  html, body {
    width: 1200px; height: 804px; overflow: hidden;
    background: var(--backdrop);
    font-family: "Open Sans", Arial, sans-serif;
  }
  .card {
    position: absolute; left: 100px; top: 122px;
    width: 1000px; height: 560px;
    border-radius: 28px; overflow: hidden;
    background: var(--card-white);
    box-shadow: 0 14px 32px rgba(0,0,0,0.18);
  }
  .card-art { position: absolute; inset: 0; }
  .brand-name {
    position: absolute; left: 0; right: 0; top: 128px;
    text-align: center;
    font-size: 50px; font-weight: 700; letter-spacing: 4px;
    text-transform: uppercase;
    color: var(--brand-red);
  }
  .holder {
    position: absolute; right: 535px; top: 370px;
    text-align: right; color: var(--ink-light);
  }
  .holder-name { font-size: 27px; font-weight: 600; line-height: 1.25; }
  .holder-title { font-size: 19px; font-weight: 400; color: var(--ink-soft); }
  .divider {
    position: absolute; left: 490px; top: 338px;
    width: 1px; height: 190px; background: rgba(255,255,255,0.6);
  }
  .contact {
    position: absolute; left: 518px; top: 340px;
    color: var(--ink-light); font-size: 19px; line-height: 29px;
    list-style: none;
  }
  .contact .address { margin-bottom: 14px; }
  .contact-line { display: flex; align-items: center; gap: 12px; }
  .contact-line svg { width: 17px; height: 17px; flex: none; }
</style>
</head>
<body>
  <div class="card">
    <svg class="card-art" viewBox="0 0 1000 560" preserveAspectRatio="none" aria-hidden="true">
      <defs>
        <linearGradient id="redPanel" x1="0" y1="0" x2="1" y2="0">
          <stop offset="0" stop-color="#b8141c"/>
          <stop offset="0.38" stop-color="#e2222b"/>
          <stop offset="0.62" stop-color="#9a141b"/>
          <stop offset="1" stop-color="#4f0c10"/>
        </linearGradient>
        <linearGradient id="blueSwoosh" x1="0" y1="0" x2="1" y2="0">
          <stop offset="0" stop-color="#183f66"/>
          <stop offset="0.5" stop-color="#2f7fb4"/>
          <stop offset="1" stop-color="#183f66"/>
        </linearGradient>
      </defs>
      <path d="M0,292 C280,205 600,310 1000,205 L1000,238 C600,325 300,238 0,306 Z" fill="url(#blueSwoosh)"/>
      <path d="M0,306 C300,238 600,325 1000,238 L1000,560 L0,560 Z" fill="url(#redPanel)"/>
    </svg>

    <div class="brand-name">Skyline Assessors</div>

    <div class="holder">
      <div class="holder-name">Corwin Hask</div>
      <div class="holder-title">Certified Appraiser</div>
    </div>

    <div class="divider"></div>

    <ul class="contact">
      <li class="address">48270 Millbrook Lane #1174<br>Sterling, VA 20391</li>
      <li class="contact-line">
        <svg viewBox="0 0 16 16" aria-hidden="true"><rect x="4" y="1" width="8" height="14" rx="1.5" fill="#fff"/><rect x="5.5" y="3" width="5" height="8" fill="#8e1b20"/></svg>
        3015550142
      </li>
      <li class="contact-line">
        <svg viewBox="0 0 16 16" aria-hidden="true"><rect x="1" y="3" width="14" height="10" rx="1" fill="#fff"/><path d="M1.5,3.5 L8,9 L14.5,3.5" fill="none" stroke="#8e1b20" stroke-width="1.3"/></svg>
        corwin@plumvexa.com
      </li>
      <li class="contact-line">
        <svg viewBox="0 0 16 16" aria-hidden="true"><circle cx="8" cy="8" r="7" fill="#fff"/><path d="M1.5,8 H14.5 M8,1 C5,4 5,12 8,15 M8,1 C11,4 11,12 8,15" fill="none" stroke="#6e1218" stroke-width="1"/></svg>
        www.plumvexa.com
      </li>
    </ul>
  </div>
</body>
</html>
```